Offshore Energy Projects Management Consultancy needs a business card design

Logo available. We provide teams to deliver engineering consultancy, project management and delivery teams mainly in the offshore renewables sector. The company is all about bringing the right people to a project to deliver the scope.

The business card will be used for all staff.

The business card should be quite simple, vibrant and uncluttered but convey experience, enthusiasm and integration.

Target Market(s)

Energy Project Developers and Tier 1 construction companies

Contact Information for Business Card

Logo should be on the back of the card. I'm happy for the designer to play with the colour of the logo and background colour.

Front of the card should convey all the must have information in a clear and professional manner but without being overly traditional.

Colors

Designer to choose colors to be used in the design.

Requirements
Must have
• Land Line Tel Number, Mobile Tel Number, Email, business address, web address.

```html
<!DOCTYPE html>
<html lang="en">
<head>
<meta charset="utf-8">
<title>Seaward Works Collective – Business Card</title>
<link rel="stylesheet" href="https://fonts.googleapis.com/css2?family=Lato:wght@400;700;900&display=swap">
<style>
  :root {
    --page-bg: #e6e7e9;
    --card-bg: #f7f7f7;
    --card-shade: #ececec;
    --edge-blue: #1466b8;
    --navy-blue: #1565b0;
    --sky-blue: #1f97d1;
    --ink-grey: #5b5d61;
    --icon-blue: #1a6fbf;
  }
  * { box-sizing: border-box; margin: 0; padding: 0; }
  html, body { width: 1200px; height: 900px; overflow: hidden; }
  body {
    background: var(--page-bg);
    font-family: "Lato", Arial, sans-serif;
    position: relative;
  }
  .card {
    position: absolute;
    left: 250px;
    width: 700px;
    height: 400px;
    background: linear-gradient(160deg, var(--card-bg) 0%, var(--card-shade) 100%);
    border-left: 5px solid var(--edge-blue);
    border-bottom: 7px solid var(--edge-blue);
    box-shadow: 0 10px 24px rgba(0,0,0,0.18);
  }
  .card--front { top: 40px; }
  .card--back { top: 470px; }

  /* brand stand-in */
  .brand {
    display: flex;
    align-items: center;
    gap: 12px;
    color: var(--navy-blue);
    font-weight: 900;
    text-transform: uppercase;
    letter-spacing: 0.04em;
  }
  .brand__dot {
    flex: none;
    border-radius: 50%;
    background: var(--sky-blue);
  }
  .card--front .brand {
    position: absolute;
    left: 40px;
    top: 170px;
    width: 330px;
    font-size: 22px;
    line-height: 1.2;
  }
  .card--front .brand__dot { width: 44px; height: 44px; }

  .divider {
    position: absolute;
    left: 395px;
    top: 95px;
    width: 2px;
    height: 210px;
    background: var(--edge-blue);
  }

  .contact {
    position: absolute;
    left: 430px;
    top: 90px;
  }
  .contact__name {
    font-size: 30px;
    font-weight: 700;
    letter-spacing: 0.01em;
    line-height: 1;
  }
  .contact__first { color: var(--navy-blue); }
  .contact__last { color: var(--sky-blue); }
  .contact__role {
    font-size: 17px;
    color: var(--ink-grey);
    margin-top: 6px;
    letter-spacing: 0.03em;
  }
  .contact__list {
    list-style: none;
    margin-top: 18px;
  }
  .contact__item {
    display: flex;
    align-items: center;
    gap: 14px;
    height: 34px;
    font-size: 17px;
    color: var(--ink-grey);
    letter-spacing: 0.02em;
  }
  .contact__icon { width: 22px; height: 22px; flex: none; }

  .card--back .brand {
    position: absolute;
    left: 0; right: 0;
    top: 160px;
    justify-content: center;
    font-size: 36px;
  }
  .card--back .brand__dot { width: 60px; height: 60px; }
</style>
</head>
<body>

<section class="card card--front" aria-label="Card front">
  <div class="brand">
    <span class="brand__dot"></span>
    <span class="brand__name">Seaward Works Collective</span>
  </div>

  <div class="divider"></div>

  <div class="contact">
    <p class="contact__name"><span class="contact__first">DANIEL</span> <span class="contact__last">HART</span></p>
    <p class="contact__role">Founder &amp; CEO</p>
    <ul class="contact__list">
      <li class="contact__item">
        <svg class="contact__icon" viewBox="0 0 24 24" aria-hidden="true">
          <rect x="6" y="2" width="12" height="20" rx="2" fill="none" stroke="var(--icon-blue)" stroke-width="2"/>
          <circle cx="12" cy="18" r="1.3" fill="var(--icon-blue)"/>
        </svg>
        555-014 2231
      </li>
      <li class="contact__item">
        <svg class="contact__icon" viewBox="0 0 24 24" aria-hidden="true">
          <path d="M2 9c2-4 18-4 20 0l-1 3h-4l-1-3H8l-1 3H3z" fill="var(--icon-blue)"/>
          <rect x="4" y="12" width="16" height="9" rx="1.5" fill="var(--icon-blue)"/>
          <circle cx="12" cy="16.5" r="2.4" fill="#fff"/>
        </svg>
        555-017 4480
      </li>
      <li class="contact__item">
        <svg class="contact__icon" viewBox="0 0 24 24" aria-hidden="true">
          <rect x="2" y="5" width="20" height="14" fill="var(--icon-blue)"/>
          <path d="M2 5l10 8 10-8" fill="none" stroke="#fff" stroke-width="1.6"/>
        </svg>
        hello@seawardworks.co
      </li>
      <li class="contact__item">
        <svg class="contact__icon" viewBox="0 0 24 24" aria-hidden="true">
          <circle cx="12" cy="12" r="10" fill="none" stroke="var(--icon-blue)" stroke-width="2"/>
          <ellipse cx="12" cy="12" rx="4.5" ry="10" fill="none" stroke="var(--icon-blue)" stroke-width="1.5"/>
          <path d="M2 12h20M4 7h16M4 17h16" stroke="var(--icon-blue)" stroke-width="1.5"/>
        </svg>
        www.seawardworks.co
      </li>
    </ul>
  </div>
</section>

<section class="card card--back" aria-label="Card back">
  <div class="brand">
    <span class="brand__dot"></span>
    <span class="brand__name">Seaward Works Collective</span>
  </div>
</section>

</body>
</html>
```